Velo Crest Business Card

Need a professional but with a touch of unique looking Business Card for my staff.

Target Market(s)

Corporate

Industry/Entity Type

Business

Requirements
Must have
• 40mm height

```html
<!DOCTYPE html>
<html lang="en">
<head>
<meta charset="utf-8">
<title>Velo Crest Business Card</title>
<link rel="stylesheet" href="https://fonts.googleapis.com/css2?family=Open+Sans:wght@400;600&display=swap">
<style>
  :root {
    --page-bg: #eeeeee;
    --front-dark: #141414;
    --front-mid: #262626;
    --back-light: #3aa6d4;
    --back-dark: #1f86b8;
    --accent-blue: #2fa8de;
    --ink-white: #ffffff;
    --ink-soft: #e4e4e4;
    --icon-fill: #d9d9d9;
  }
  html, body {
    margin: 0;
    width: 1200px;
    height: 800px;
    overflow: hidden;
    background: var(--page-bg);
    font-family: "Open Sans", Arial, sans-serif;
  }
  .stage { position: relative; width: 1200px; height: 800px; }
  .card {
    position: absolute;
    left: 300px;
    width: 600px;
    height: 267px;
    overflow: hidden;
  }
  .card-front {
    top: 133px;
    background: linear-gradient(135deg, var(--front-mid), var(--front-dark));
  }
  .card-back {
    top: 400px;
    background: radial-gradient(ellipse at 50% 40%, var(--back-light), var(--back-dark));
  }
  .card-lines { position: absolute; inset: 0; }
  .wordmark {
    position: absolute;
    margin: 0;
    color: var(--ink-white);
    font-weight: 400;
    letter-spacing: -1px;
    line-height: 1;
  }
  .card-front .wordmark { left: 18px; top: 120px; font-size: 54px; }
  .card-back .wordmark { left: 0; right: 0; top: 104px; text-align: center; font-size: 62px; }
  .holder {
    position: absolute;
    right: 42px;
    top: 42px;
    text-align: right;
  }
  .holder-name { margin: 0; color: var(--ink-white); font-size: 27px; font-weight: 400; line-height: 1.1; }
  .holder-role { margin: 0; color: var(--accent-blue); font-size: 15px; line-height: 1.1; padding-right: 38px; }
  .contact-list { list-style: none; margin: 0; padding: 0; }
  .contact-item {
    position: absolute;
    display: flex;
    align-items: center;
    gap: 12px;
    color: var(--ink-soft);
    font-size: 16px;
    line-height: 1;
    white-space: nowrap;
  }
  .contact-icon { width: 14px; height: 14px; flex: none; }
</style>
</head>
<body>
<main class="stage">

  <section class="card card-front" aria-label="Card front">
    <svg class="card-lines" width="600" height="267" viewBox="0 0 600 267" aria-hidden="true">
      <line x1="358" y1="0" x2="318" y2="267" stroke="var(--ink-white)" stroke-width="3"/>
      <line x1="372" y1="0" x2="332" y2="267" stroke="var(--accent-blue)" stroke-width="3"/>
    </svg>
    <p class="wordmark">velocrest</p>
    <div class="holder">
      <h1 class="holder-name">Daniel Marsh</h1>
      <p class="holder-role">ceo</p>
    </div>
    <ul class="contact-list">
      <li class="contact-item" style="left:368px; top:127px">
        <svg class="contact-icon" viewBox="0 0 14 14" aria-hidden="true"><circle cx="7" cy="7" r="7" fill="var(--icon-fill)"/><path d="M4.5 3.5 L6 3.5 L6.6 5.4 L5.6 6.2 Q6.5 7.8 7.9 8.5 L8.7 7.5 L10.5 8.1 L10.5 9.6 Q6 10.2 4.5 3.5Z" fill="var(--front-dark)"/></svg>
        <span>(555) 214-7780</span>
      </li>
      <li class="contact-item" style="left:363px; top:155px">
        <svg class="contact-icon" viewBox="0 0 14 14" aria-hidden="true"><circle cx="7" cy="7" r="7" fill="var(--icon-fill)"/><rect x="3.5" y="4.5" width="7" height="5" fill="var(--front-dark)"/><path d="M3.5 4.5 L7 7.3 L10.5 4.5" stroke="var(--icon-fill)" stroke-width="0.8" fill="none"/></svg>
        <span>danielmarsh@mailbox.com</span>
      </li>
      <li class="contact-item" style="left:357px; top:182px">
        <svg class="contact-icon" viewBox="0 0 14 14" aria-hidden="true"><circle cx="7" cy="7" r="7" fill="var(--icon-fill)"/><circle cx="7" cy="7" r="3.6" fill="none" stroke="var(--front-dark)" stroke-width="1"/><line x1="3.4" y1="7" x2="10.6" y2="7" stroke="var(--front-dark)" stroke-width="0.8"/><ellipse cx="7" cy="7" rx="1.5" ry="3.6" fill="none" stroke="var(--front-dark)" stroke-width="0.8"/></svg>
        <span>www.velocrest.com</span>
      </li>
      <li class="contact-item" style="left:352px; top:209px">
        <svg class="contact-icon" viewBox="0 0 14 14" aria-hidden="true"><circle cx="7" cy="7" r="7" fill="var(--icon-fill)"/></svg>
        <span>linkup.com/danielmarsh</span>
      </li>
      <li class="contact-item" style="left:346px; top:235px">
        <svg class="contact-icon" viewBox="0 0 14 14" aria-hidden="true"><circle cx="7" cy="7" r="7" fill="var(--icon-fill)"/></svg>
        <span>chirper.com/danielmarsh</span>
      </li>
    </ul>
  </section>

  <section class="card card-back" aria-label="Card back">
    <svg class="card-lines" width="600" height="267" viewBox="0 0 600 267" aria-hidden="true">
      <line x1="128" y1="0" x2="80" y2="267" stroke="var(--ink-white)" stroke-opacity="0.7" stroke-width="2"/>
      <line x1="138" y1="0" x2="90" y2="267" stroke="var(--ink-white)" stroke-opacity="0.35" stroke-width="2"/>
      <line x1="530" y1="0" x2="490" y2="267" stroke="var(--ink-white)" stroke-opacity="0.7" stroke-width="2"/>
      <line x1="540" y1="0" x2="500" y2="267" stroke="var(--ink-white)" stroke-opacity="0.35" stroke-width="2"/>
    </svg>
    <p class="wordmark">velocrest</p>
  </section>

</main>
</body>
</html>
```